Mortgage Broker Site

Need a custom design for a mortgage broker site - please refer to the attached Word .doc that gives more detail.

Number of Pages Required

5+ page

Colors

Designer to choose colors to be used in the design.

```html
<!DOCTYPE html>
<html lang="en">
<head>
<meta charset="utf-8">
<title>Halvera — Mortgage Broker</title>
<link rel="stylesheet" href="https://fonts.googleapis.com/css2?family=Montserrat:wght@500;600;700&family=Raleway:wght@400;500;600;700&display=swap">
<style>
:root{
  --ink:#1b1b1b;
  --dark:#222a33;
  --red:#d0002c;
  --red-deep:#7a0016;
  --red-mid:#8c001b;
  --grey:#8a8f96;
  --light:#f3f4f8;
  --orange:#f07d1a;
  --white:#fff;
}
*{box-sizing:border-box;margin:0;padding:0}
html,body{width:1200px;height:2541px;overflow:hidden}
body{position:relative;background:var(--white);font-family:Raleway,sans-serif;color:var(--ink)}
.abs{position:absolute}
.heading{font-family:Montserrat,sans-serif;font-weight:700}

/* top bar */
.topbar{left:0;top:0;width:1200px;height:43px;background:var(--dark);color:#e8e8e8;font-size:11px}
.topbar .item{top:14px;display:flex;align-items:center;gap:8px}
.topbar svg{width:11px;height:11px;fill:#3fa2e0}
.social{display:flex;gap:8px}
.social span{display:block;width:20px;height:20px;background:#56606b;border-radius:2px}

/* header */
.header{left:0;top:43px;width:1200px;height:82px;border-bottom:3px solid var(--red);background:var(--white)}
.logo{left:166px;top:26px;display:flex;align-items:center;gap:8px;font-family:Montserrat,sans-serif;font-weight:600;font-size:28px;color:var(--ink)}
.logo i{display:block;width:12px;height:12px;background:var(--red)}
.nav{top:34px;font-family:Montserrat,sans-serif;font-weight:500;font-size:12px;color:var(--ink)}
.nav.active{color:var(--red)}
.apply{left:970px;top:31px;background:var(--red);color:#fff;font-family:Montserrat,sans-serif;font-weight:600;font-size:12px;padding:3px 6px;border-radius:5px}

/* hero */
.hero{left:0;top:125px;width:1200px;height:406px;background:linear-gradient(110deg,#e0052f 0%,#c4002a 45%,#a2001e 100%)}
.hero h1{left:160px;top:118px;font-size:38px;line-height:42px;color:#fff;letter-spacing:.5px}
.hero p{left:160px;top:210px;width:300px;font-family:Montserrat,sans-serif;font-weight:700;font-size:9.5px;line-height:11px;color:#fff;text-transform:uppercase}
.hero .cta{left:161px;top:286px;width:196px;height:44px;background:#b7001f;border-radius:4px;color:#fff;font-family:Montserrat,sans-serif;font-weight:600;font-size:15px;display:flex;align-items:center;justify-content:center}

/* tools */
.tools-title{left:0;width:1200px;top:560px;text-align:center;font-size:33px;color:#111}
.tools-sub{left:0;width:1200px;top:618px;text-align:center;font-size:13px;color:#9a9ea4}
.tool{top:675px;width:280px;height:178px;text-align:center;border-bottom:1px solid #eee}
.tool.first{border-right:1px solid #eee}
.tool .icon{width:66px;height:66px;margin:8px auto 0}
.tool h3{margin-top:18px;font-size:16px;font-weight:600;font-family:Raleway,sans-serif}
.tool p{margin:8px auto 0;width:240px;font-size:11px;line-height:16px;color:#555}

/* about */
.about-bg{left:0;top:888px;width:1200px;height:532px;background:linear-gradient(90deg,#c9ccd0 0%,#dfe1e3 40%,#e9eaec 70%,#b9bcc0 100%)}
.about-panel{left:575px;top:945px;width:328px;height:398px;background:var(--red-deep);padding:52px 42px 0}
.about-panel h2{font-family:Montserrat,sans-serif;font-weight:600;font-size:33px;color:#fff}
.about-panel .lead{margin-top:30px;font-size:10.5px;line-height:18.5px;color:#ff6f7c}
.about-panel ul{list-style:none;margin-top:14px}
.about-panel li{display:flex;align-items:center;gap:10px;font-size:10.5px;color:#fff;height:27px}
.about-panel li svg{width:14px;height:10px;stroke:#ff6f7c;fill:none;stroke-width:1.6}
.about-panel .btn{margin-top:32px;width:194px;height:38px;border:2px solid #fff;border-radius:3px;display:flex;align-items:center;justify-content:center;color:#fff;font-family:Montserrat,sans-serif;font-weight:700;font-size:10px;gap:8px}
.stats{left:903px;top:975px;width:129px;height:337px;background:var(--red-mid)}
.stat{height:115px;border-bottom:1px solid #a8303f;text-align:center;padding-top:30px}
.stat:last-child{border-bottom:0;height:107px}
.stat b{display:block;font-family:Raleway,sans-serif;font-weight:700;font-size:34px;color:#fff;line-height:34px}
.stat span{font-size:10px;color:#e0606d}

/* calculator */
.calc-head{left:163px;top:1493px;display:flex;align-items:center;gap:10px;font-size:28px;color:#111}
.calc-head svg{width:36px;height:36px}
.label{font-size:10.5px;color:#8b8f95}
.field{width:190px;height:40px;background:var(--light);border-radius:2px;font-size:11px;color:#555;display:flex;align-items:center;justify-content:space-between;padding:0 13px}
.field svg{width:10px;height:6px;stroke:var(--orange);fill:none;stroke-width:2}
.field.total{border-bottom:2px solid var(--orange)}
.calc-photo{left:645px;top:1468px;width:370px;height:330px;background:linear-gradient(135deg,#f4f4f4 0%,#e1e3e6 55%,#b9c0cb 100%)}

/* news */
.news-title{left:0;width:1200px;top:1887px;text-align:center;font-family:Raleway,sans-serif;font-weight:600;font-size:34px;color:#111}
.card{top:1960px;width:200px;height:227px;border-bottom:1px solid #e6e6e6}
.card .photo{height:136px}
.card h4{margin:16px 15px 0;font-size:12px;line-height:18px;font-weight:600;color:#222}
.card .meta{margin:8px 15px 0;font-size:8px;color:#a0a4a9}
.card .meta em{font-style:normal;color:var(--orange);margin-left:12px}
.card .meta i{font-style:normal;margin-left:10px;color:#ccc}

/* footer */
.footer{left:0;top:2266px;width:1200px;height:275px;background:var(--dark);color:#fff}
.footer h5{font-family:Montserrat,sans-serif;font-weight:700;font-size:12.5px}
.footer .about{width:225px;font-family:Montserrat,sans-serif;font-weight:600;font-size:7.5px;line-height:9.5px;text-transform:uppercase}
.links{font-size:10.5px;line-height:29px}
.links div{display:flex;align-items:center;gap:10px}
.links div::before{content:"›";color:#3fa2e0;font-size:13px}
.subscribe{display:flex}
.subscribe .input{width:230px;height:40px;background:#fff;color:#9a9ea4;font-size:10px;display:flex;align-items:center;padding-left:15px}
.subscribe .send{width:45px;height:40px;background:var(--red);display:flex;align-items:center;justify-content:center}
.to-top{left:1144px;top:2488px;width:32px;height:32px;border-radius:50%;background:#c7001f;display:flex;align-items:center;justify-content:center}
.foot-logo{left:0;width:1200px;top:2519px;text-align:center;font-family:Montserrat,sans-serif;font-weight:600;font-size:13px}
</style>
</head>
<body>

<!-- top bar -->
<div class="abs topbar">
  <div class="abs item" style="left:155px">
    <svg viewBox="0 0 12 12"><path d="M6 0a4 4 0 0 0-4 4c0 3 4 8 4 8s4-5 4-8a4 4 0 0 0-4-4zm0 5.5A1.5 1.5 0 1 1 6 2.5a1.5 1.5 0 0 1 0 3z"/></svg>
    48 Harbor Lane Brookfield, NY 10455
  </div>
  <div class="abs item" style="left:394px">
    <svg viewBox="0 0 12 12"><circle cx="6" cy="6" r="5" fill="none" stroke="#3fa2e0" stroke-width="1.5"/><path d="M6 3v3.3l2 1.2" stroke="#3fa2e0" stroke-width="1.2" fill="none"/></svg>
    Mon – Sat: 9:00am–18:00pm. Sunday closed
  </div>
  <div class="abs item" style="left:668px">
    <svg viewBox="0 0 12 12"><path d="M2.5 0.8l2 2.3-1 1.4a7 7 0 0 0 4 4l1.4-1 2.3 2-1.2 1.8C5 11 1 7 0.7 2z"/></svg>
    <span style="margin-left:6px">(555) 214-7730</span>
  </div>
  <div class="abs social" style="left:970px;top:11px"><span></span><span></span><span></span></div>
</div>

<!-- header -->
<header class="abs header">
  <div class="abs logo">Halvera<i></i></div>
  <nav>
    <span class="abs nav active" style="left:506px">HOME</span>
    <span class="abs nav" style="left:574px">ABOUT US</span>
    <span class="abs nav" style="left:664px">GUIDES</span>
    <span class="abs nav" style="left:739px">SCHEDULE A CALL</span>
    <span class="abs nav" style="left:883px">SERVICES</span>
    <span class="abs apply">APPLY NOW</span>
  </nav>
</header>

<!-- hero -->
<section class="abs hero" role="img" aria-label="Red-tinted photograph of glass office towers seen from below">
  <h1 class="abs heading">WRITE YOUR TEXT<br>HERE</h1>
  <p class="abs">Lorem ipsum dolor sit amet, consectetur adipiscing elit, sed do eiusmod tempor incididunt ut labore et dolore magna aliqua. Quis ipsum suspendisse ultrices gravida. Risus commodo viverra maecenas accumsan lacus vel facilisis.</p>
  <div class="abs cta">GET APOIPMENT NOW</div>
</section>

<!-- mortgage tools -->
<h2 class="abs heading tools-title">MORTGAGE TOOLS</h2>
<p class="abs tools-sub">We provide expert tax and advisory services to individuals and small businesses.</p>

<div class="abs tool first" style="left:295px">
  <svg class="icon" viewBox="0 0 66 66">
    <polygon points="33,1 61,17 61,49 33,65 5,49 5,17" fill="#f1f2f7"/>
    <g fill="none" stroke="#222" stroke-width="1.5">
      <rect x="21" y="24" width="24" height="22"/><path d="M25 24v-4h16v4M33 16v4"/>
      <rect x="24" y="28" width="4" height="4"/><rect x="31" y="28" width="4" height="4"/><rect x="38" y="28" width="4" height="4"/>
      <rect x="24" y="35" width="4" height="4"/><rect x="38" y="35" width="4" height="4"/><rect x="31" y="38" width="4" height="8"/>
    </g>
  </svg>
  <h3>Mortgage Calculator</h3>
  <p>See how much you can afford by home price, monthly payment, or income</p>
</div>

<div class="abs tool" style="left:575px;width:295px">
  <svg class="icon" viewBox="0 0 66 66">
    <polygon points="33,1 61,17 61,49 33,65 5,49 5,17" fill="#f1f2f7"/>
    <g fill="none" stroke="#222" stroke-width="1.5">
      <rect x="17" y="23" width="32" height="20"/><rect x="20" y="26" width="26" height="14"/>
      <circle cx="33" cy="33" r="5"/><path d="M33 30v6M31.5 31.5h3M31.5 34.5h3"/>
    </g>
  </svg>
  <h3>Home Value Checker</h3>
  <p>Should you refinance? This calculator breaks down monthly and lifetime cost</p>
</div>

<!-- about -->
<section class="abs about-bg" role="img" aria-label="Photograph of a smiling senior consultant with crossed arms in a bright office"></section>
<div class="abs about-panel">
  <h2>About Us</h2>
  <p class="lead">We are dedicated to providing professional service with the highest degree of honesty and integrity, and strive to add value to our tax and consulting services.</p>
  <ul>
    <li><svg viewBox="0 0 14 10"><path d="M1 5l4 4 8-8"/></svg>Highly Competent Professionals;</li>
    <li><svg viewBox="0 0 14 10"><path d="M1 5l4 4 8-8"/></svg>Affordable Prices;</li>
    <li><svg viewBox="0 0 14 10"><path d="M1 5l4 4 8-8"/></svg>High Successful Recovery.</li>
  </ul>
  <div class="btn">MAKE AN APPOINTMENT <span>›</span></div>
</div>
<div class="abs stats">
  <div class="stat"><b>23</b><span>Consultants</span></div>
  <div class="stat"><b>546</b><span>Happy Clients</span></div>
  <div class="stat"><b>17</b><span>Years of Experience</span></div>
</div>

<!-- calculator -->
<div class="abs calc-head heading">
  <svg viewBox="0 0 36 36" fill="none" stroke="#3fa2e0" stroke-width="1.5">
    <rect x="2" y="2" width="32" height="32" rx="2"/><path d="M18 2v32M2 18h32M7 10h6M10 7v6M23 10h6M7 26h6M23 24h6M23 28h6M8 22l4 4M12 22l-4 4"/>
  </svg>
  MORTGAGE CALCULATOR
</div>

<div class="abs label" style="left:164px;top:1557px">Choose your business area</div>
<div class="abs field" style="left:164px;top:1577px">Retail<svg viewBox="0 0 10 6"><path d="M1 1l4 4 4-4"/></svg></div>
<div class="abs label" style="left:375px;top:1557px">Country of residence</div>
<div class="abs field" style="left:375px;top:1577px">USA<svg viewBox="0 0 10 6"><path d="M1 1l4 4 4-4"/></svg></div>
<div class="abs label" style="left:164px;top:1635px">Employees number</div>
<div class="abs field" style="left:164px;top:1655px">1-5<svg viewBox="0 0 10 6"><path d="M1 1l4 4 4-4"/></svg></div>
<div class="abs label" style="left:375px;top:1635px">Yearly Income</div>
<div class="abs field" style="left:375px;top:1655px"></div>
<div class="abs label" style="left:164px;top:1713px">Total Payment</div>
<div class="abs field total" style="left:164px;top:1733px;height:42px"></div>

<div class="abs calc-photo" role="img" aria-label="Illustration of tax forms with a blue pen and a desk calculator"></div>

<!-- news -->
<h2 class="abs news-title">Latest News</h2>

<article class="abs card" style="left:168px">
  <div class="photo" role="img" aria-label="Photo of hands reviewing financial charts" style="background:linear-gradient(135deg,#dfe6f2,#b7c6de)"></div>
  <h4>The Top 5 Tax Paper Downloads</h4>
  <div class="meta">JUNE 14, 2017<i>|</i><em>BY LEO MARSH</em></div>
</article>
<article class="abs card" style="left:391px">
  <div class="photo" role="img" aria-label="Photo of a hand writing next to a calculator" style="background:linear-gradient(135deg,#f2f2f2,#cfd2d6)"></div>
  <h4>Exploring American Taxes: Then &amp; Now</h4>
  <div class="meta">JUNE 20, 2017<i>|</i><em>BY NORA QUILL</em></div>
</article>
<article class="abs card" style="left:614px">
  <div class="photo" role="img" aria-label="Photo of two colleagues working at a laptop" style="background:linear-gradient(135deg,#c9ced6,#8f97a3)"></div>
  <h4>The Tax Consequences Of Brexit</h4>
  <div class="meta">JUNE 23, 2017<i>|</i><em>BY IRIS DALTON</em></div>
</article>
<article class="abs card" style="left:837px">
  <div class="photo" role="img" aria-label="Photo of an adviser showing a document to a client" style="background:linear-gradient(135deg,#d7c9b8,#8e949c)"></div>
  <h4>What You Need to File Your Taxes This Year</h4>
  <div class="meta">JUNE 12, 2017<i>|</i><em>BY OWEN FAIRLEY</em></div>
</article>

<!-- footer -->
<footer class="abs footer">
  <h5 class="abs" style="left:168px;top:48px">ABOUT US</h5>
  <p class="abs about" style="left:168px;top:82px">Lorem ipsum dolor sit amet, consectetur adipiscing elit, sed do eiusmod tempor incididunt ut labore et dolore magna aliqua. Quis ipsum suspendisse ultrices gravida. Risus commodo viverra maecenas accumsan lacus vel facilisis.</p>
  <div class="abs" style="left:168px;top:160px;display:flex;align-items:center;gap:6px;font-size:14px">
    <svg viewBox="0 0 12 12" width="11" height="11"><path fill="#f07d1a" d="M2.5 0.8l2 2.3-1 1.4a7 7 0 0 0 4 4l1.4-1 2.3 2-1.2 1.8C5 11 1 7 0.7 2z"/></svg>
    (555) 214-7730
  </div>
  <div class="abs social" style="left:312px;top:159px"><span></span><span></span><span></span></div>

  <h5 class="abs" style="left:465px;top:48px">QUICK LINKS</h5>
  <div class="abs links" style="left:465px;top:76px"><div>Home</div><div>Services</div><div>Careers</div><div>Blog</div></div>
  <div class="abs links" style="left:595px;top:76px"><div>About us</div><div>Contacts</div><div>Appointment</div></div>

  <h5 class="abs" style="left:763px;top:48px">SUBSCRIBE</h5>
  <p class="abs" style="left:763px;top:86px;font-size:9.5px;color:#3f4853">Get the latest updates and offers.</p>
  <div class="abs subscribe" style="left:763px;top:114px">
    <div class="input">Enter Your E-mail</div>
    <div class="send"><svg width="18" height="13" viewBox="0 0 18 13" fill="none" stroke="#fff" stroke-width="1.4"><rect x="1" y="1" width="16" height="11"/><path d="M1 1l8 6 8-6"/></svg></div>
  </div>
</footer>
<div class="abs to-top"><svg width="10" height="6" viewBox="0 0 10 6" fill="none" stroke="#fff" stroke-width="1.5"><path d="M1 5l4-4 4 4"/></svg></div>
<div class="abs foot-logo" style="color:#fff">Halvera</div>

</body>
</html>
```